HSPT Foldable Flyer

Design a flyer, foldable. To fit in an envelope and/or drop off at doctor office for an outpatient physical therapy clinic, Harborstrengthpt.com.
Emphasis on appointments two weeks out, taking new patients, and use website for photos

```html
<!DOCTYPE html>
<html lang="en">
<head>
<meta charset="utf-8">
<title>Harbor Strength Physical Therapy – New Patients Flyer</title>
<link rel="stylesheet" href="https://fonts.googleapis.com/css2?family=Montserrat:wght@600;700;800&family=Raleway:wght@300;400;500&family=Exo+2:wght@600&display=swap">
<style>
  :root{
    --brand-blue:#1b5e87;
    --paper:#f4f4f4;
    --ink:#262626;
    --body-grey:#4a4a4a;
    --logo-grey:#6b7480;
    --photo-light:#d9dde0;
    --photo-mid:#7d8a93;
    --photo-warm:#c9bfa4;
    --photo-plaid:#6b5a55;
    --white:#ffffff;
  }
  *{margin:0;padding:0;box-sizing:border-box}
  html,body{width:848px;height:1200px;overflow:hidden;background:var(--paper)}
  .flyer{position:relative;width:848px;height:1200px;background:var(--paper);overflow:hidden;font-family:'Raleway',sans-serif}
  .art{position:absolute;inset:0;width:848px;height:1200px}
  .brand{position:absolute;top:18px;left:596px;display:flex;align-items:flex-start;gap:10px}
  .brand-dot{width:26px;height:26px;border-radius:50%;background:var(--brand-blue);margin-top:10px}
  .brand-name{font-family:'Exo 2',sans-serif;font-weight:600;font-size:27px;line-height:26px;color:var(--logo-grey)}
  .brand-tag{font-family:'Raleway',sans-serif;font-weight:500;font-size:10.5px;letter-spacing:1.4px;color:var(--logo-grey);margin-top:6px}
  .badge{position:absolute;left:97px;top:442px;width:176px;height:176px;display:flex;flex-direction:column;align-items:center;justify-content:center;text-align:center}
  .badge-lead{font-family:'Montserrat',sans-serif;font-weight:600;font-size:14px;color:#7c7c7c;letter-spacing:.3px}
  .badge-main{font-family:'Montserrat',sans-serif;font-weight:700;font-size:23px;line-height:26px;color:var(--brand-blue);margin-top:4px}
  .copy{position:absolute;left:64px;top:768px;width:740px}
  .availability{font-family:'Montserrat',sans-serif;font-weight:700;font-size:22.5px;color:var(--ink);letter-spacing:.1px}
  .headline{margin-top:12px;color:var(--brand-blue);line-height:1}
  .headline-strong{display:block;font-family:'Montserrat',sans-serif;font-weight:800;font-size:59px;letter-spacing:.5px}
  .headline-light{display:block;font-family:'Raleway',sans-serif;font-weight:300;font-size:61px;margin-top:6px;letter-spacing:.5px}
  .about{margin-top:12px;font-size:14px;line-height:21.5px;color:var(--body-grey);width:712px}
  .contact{position:absolute;right:83px;top:1062px;text-align:right;color:var(--white)}
  .social{display:flex;justify-content:flex-end;gap:10px}
  .social span{width:21px;height:21px;border-radius:50%;background:var(--white)}
  .web{font-family:'Montserrat',sans-serif;font-weight:700;font-size:19.5px;margin-top:10px}
  .address{font-family:'Raleway',sans-serif;font-weight:500;font-size:13.5px;margin-top:14px}
  .lines{display:flex;justify-content:flex-end;align-items:center;margin-top:10px;font-family:'Raleway',sans-serif;font-weight:500;font-size:14px}
  .lines .divider{width:1px;height:26px;background:rgba(255,255,255,.6);margin:0 20px}
</style>
</head>
<body>
<div class="flyer">
  <svg class="art" viewBox="0 0 848 1200">
    <defs>
      <linearGradient id="trainingTones" x1="0" y1="0" x2="1" y2="1">
        <stop offset="0" stop-color="var(--photo-light)"/>
        <stop offset="0.6" stop-color="var(--photo-mid)"/>
        <stop offset="1" stop-color="#3d4a54"/>
      </linearGradient>
      <linearGradient id="teamTones" x1="0" y1="0" x2="0" y2="1">
        <stop offset="0" stop-color="var(--photo-warm)"/>
        <stop offset="1" stop-color="var(--photo-plaid)"/>
      </linearGradient>
    </defs>
    <polygon fill="var(--brand-blue)" points="0,0 480,0 300,95 0,210"/>
    <polygon fill="var(--brand-blue)" points="848,55 848,215 640,340 470,425 300,505 120,610 0,692 0,525 240,460 420,370 560,262 700,150 800,85"/>
    <polygon role="img" aria-label="Photo: therapist guiding a patient through a medicine-ball balance exercise" fill="url(#trainingTones)" points="0,205 250,110 470,25 545,40 540,235 420,362 240,452 0,520"/>
    <polygon role="img" aria-label="Photo: the clinic team standing together in the treatment gym" fill="url(#teamTones)" points="848,225 848,595 700,655 560,700 420,728 275,695 255,610 300,520 470,440 640,355"/>
    <circle cx="185" cy="530" r="92" fill="var(--paper)"/>
    <circle cx="185" cy="530" r="84" fill="none" stroke="var(--brand-blue)" stroke-width="1.2" stroke-dasharray="5 3"/>
    <rect role="img" aria-label="Faint decorative line pattern" x="0" y="1060" width="195" height="140" fill="#eeeef3"/>
    <polygon fill="var(--brand-blue)" points="300,1200 380,1140 450,1110 560,1062 700,1040 800,1050 848,1072 848,1200"/>
  </svg>

  <div class="brand">
    <span class="brand-dot"></span>
    <div>
      <div class="brand-name">Harbor<br>Strength</div>
      <div class="brand-tag">PHYSICAL THERAPY</div>
    </div>
  </div>

  <div class="badge">
    <span class="badge-lead">We're welcoming</span>
    <span class="badge-main">New<br>Patients!</span>
  </div>

  <main class="copy">
    <p class="availability">Book your appointment for availability starting in two weeks.</p>
    <h1 class="headline">
      <span class="headline-strong">Helping You Move</span>
      <span class="headline-light">Better And Feel Better</span>
    </h1>
    <p class="about">Founded in the Spring of 2020, HSPT was born to provide and create an environment where the patient is put as the number one priority. We are here to provide quality one on one care, evidence based treatment and to assist in providing you with the quality of life that you deserve.</p>
  </main>

  <footer class="contact">
    <div class="social"><span></span><span></span><span></span></div>
    <div class="web">www.harborstrengthpt.com</div>
    <div class="address">2240 W. Cedar Ave, Suite B | Lodi, CA 95240</div>
    <div class="lines"><span>Info@HarborStrengthPT.com</span><span class="divider"></span><span>209-555-0148</span></div>
  </footer>
</div>
</body>
</html>
```